Label for beer can

I need a new label for my beer cans which will be printed on the cans.
See the detailed description in "Description_PDF".

I would like to extend the deadline.

```html
<!DOCTYPE html>
<html lang="de">
<head>
<meta charset="utf-8">
<title>Blondes Lager – Dosenetikett</title>
<link rel="stylesheet" href="https://fonts.googleapis.com/css2?family=Bebas+Neue&family=Poppins:wght@700;800&family=Roboto+Condensed:wght@500&display=swap">
<style>
  :root {
    --backdrop: #e3e3e3;
    --label-black: #0b0b0b;
    --label-yellow: #fff200;
    --yellow-deep: #f5d90a;
    --ink-white: #ffffff;
    --ink-black: #111111;
  }
  * { margin: 0; padding: 0; box-sizing: border-box; }
  html, body {
    width: 1200px;
    height: 800px;
    overflow: hidden;
    background: var(--backdrop);
  }
  .canvas {
    width: 1200px;
    height: 800px;
    display: flex;
    align-items: center;
    justify-content: center;
  }
  .can-label {
    display: block;
    width: 307px;
    height: 760px;
  }
  .panel-black { fill: var(--label-black); }
  .panel-yellow { fill: var(--label-yellow); }
  .accent-stripe { stroke: var(--label-yellow); stroke-width: 3; opacity: 0.85; }
  .brand-name {
    font-family: "Bebas Neue", sans-serif;
    font-size: 70px;
    letter-spacing: 1px;
  }
  .brand-name--light { fill: var(--ink-white); }
  .brand-name--dark { fill: var(--ink-black); }
  .brand-dot--light { fill: var(--ink-white); }
  .brand-dot--dark { fill: var(--ink-black); }
  .style-word {
    font-family: "Bebas Neue", sans-serif;
  }
  .style-word--blondes { fill: var(--label-yellow); font-size: 240px; }
  .style-word--lager { fill: var(--ink-black); font-size: 282px; }
  .halftone-area { fill: url(#halftoneTone); }
  .hop-area { fill: url(#hopTone); }
  .claim-box { fill: none; stroke: var(--ink-white); stroke-width: 2; }
  .claim-text {
    font-family: "Poppins", sans-serif;
    font-weight: 700;
    font-size: 19px;
    fill: var(--ink-white);
  }
  .spec-text {
    font-family: "Roboto Condensed", sans-serif;
    font-weight: 500;
    font-size: 25px;
    fill: var(--ink-black);
  }
  .spec-rule { stroke: var(--ink-black); stroke-width: 2; }
  .origin-text {
    font-family: "Poppins", sans-serif;
    font-weight: 800;
    font-size: 20px;
    fill: var(--ink-black);
  }
</style>
</head>
<body>
<main class="canvas">
  <svg class="can-label" viewBox="920 90 530 1310" xmlns="http://www.w3.org/2000/svg">
    <defs>
      <linearGradient id="halftoneTone" x1="0" y1="0" x2="0" y2="1">
        <stop offset="0" stop-color="#fff200"/>
        <stop offset="1" stop-color="#f8de1a"/>
      </linearGradient>
      <linearGradient id="hopTone" x1="0" y1="0" x2="0" y2="1">
        <stop offset="0" stop-color="#1a1a1a"/>
        <stop offset="1" stop-color="#3a3400"/>
      </linearGradient>
    </defs>

    <!-- label panels -->
    <rect class="panel-black" x="920" y="90" width="262" height="1310"/>
    <rect class="panel-yellow" x="1180" y="90" width="270" height="1310"/>

    <!-- side accent stripes -->
    <line class="accent-stripe" x1="936" y1="620" x2="936" y2="1300"/>
    <line class="accent-stripe" x1="945" y1="660" x2="945" y2="1300"/>
    <line class="accent-stripe" x1="954" y1="700" x2="954" y2="1300"/>

    <!-- brand name, black side -->
    <text class="brand-name brand-name--light" x="1050" y="253" text-anchor="middle">HELLWERK</text>
    <circle class="brand-dot--light" cx="1140" cy="228" r="9"/>

    <!-- brand name, yellow side -->
    <circle class="brand-dot--dark" cx="1215" cy="228" r="9"/>
    <text class="brand-name brand-name--dark" x="1330" y="253" text-anchor="middle">HELLWERK</text>

    <!-- style names -->
    <text class="style-word style-word--blondes" transform="translate(1168 1272) rotate(-90)" textLength="940" lengthAdjust="spacingAndGlyphs">BLONDES</text>
    <text class="style-word style-word--lager" transform="translate(1392 968) rotate(-90)" textLength="718" lengthAdjust="spacingAndGlyphs">LAGER</text>

    <!-- dotted tone field behind hop -->
    <g role="img" aria-label="Halftone dot pattern in yellow tones">
      <rect class="halftone-area" x="1188" y="1000" width="262" height="370"/>
    </g>

    <!-- hop cone illustration -->
    <g role="img" aria-label="Illustration of a hop cone in black and yellow">
      <rect class="hop-area" x="1222" y="985" width="162" height="270" rx="60"/>
    </g>

    <!-- claim box -->
    <rect class="claim-box" x="955" y="1304" width="210" height="56"/>
    <text class="claim-text" x="1060" y="1328" text-anchor="middle">NATURBELASSEN UND</text>
    <text class="claim-text" x="1060" y="1350" text-anchor="middle">UNPASTEURISIERT</text>

    <!-- specs -->
    <text class="spec-text" x="1295" y="1326" text-anchor="end">5% ALC</text>
    <line class="spec-rule" x1="1310" y1="1300" x2="1310" y2="1330"/>
    <text class="spec-text" x="1325" y="1326">440 ML</text>
    <line class="spec-rule" x1="1205" y1="1339" x2="1398" y2="1339"/>
    <text class="origin-text" x="1302" y="1365" text-anchor="middle">SWISS CRAFT BEER</text>
  </svg>
</main>
</body>
</html>
```